Funky Cloud Security Startup wants a cutting edge website

We're looking for a clean and simple website to be able to sell out cutting edge Cloud Security products. We already have a logo and business codes to give you a view of the style/colours etc (see attached). Really looking for something similar to plumvane.com , tarvimo.com and if push comes to shove then our competitors vesta harbor.com.au don't have a bad site either.

We're still working through the content sections but want to have a home for the following types of content immediately:

Products (4 of them)
Company
Technology Partners
Press/News
Contact Us
Support
Login

and the site will need to expand to accommodate

Buy
Case Studies
Channel Partners

at some point in the future

On the bottom Nav we want:
* Privacy Policy
* Terms of Use
* Contact
* WorkWeave
* Chirpnest

The home page should an image rotator on it with some suitably cool images and call to actions as text hovering over them.

We need it to be easily editable in dreamweaver so a template is a must, it should also be completely CSS driven and adaptive so will work on mobile, tablet and desktop - you know the score.

We're hosting on a linux server so PHP code for any crazy stuff is a must.

Really exciting project as this will be a huge company with major investors backing it internationally so you will be able to put your name against the next Glimmerly/Chirpnest/Coinrove.

Go crazy with your creativity, just remember vorlu's slogan is "Security made simple"

We look forward to seeing your creations, good luck!

```html
<!DOCTYPE html>
<html lang="en">
<head>
<meta charset="utf-8">
<title>vorlu — Security made simple</title>
<link href="https://fonts.googleapis.com/css2?family=Arimo:wght@400;700&display=swap" rel="stylesheet">
<style>
:root{
  --blue:#2a86c8;
  --blue-dark:#1f6aa6;
  --green:#7fb432;
  --ink:#333;
  --muted:#555;
  --light:#f4f4f4;
  --hero-top:#f1f1f1;
  --hero-bottom:#dedede;
  --footer:#5c5c5e;
  --footer-bar:#414143;
  --footer-text:#c9c9c9;
  --sky:#6fc4ef;
  --sky-pale:#cde9f8;
}
*{box-sizing:border-box;margin:0;padding:0}
html,body{width:736px;height:1200px;overflow:hidden}
body{font-family:"Arimo",Arial,sans-serif;color:var(--ink);background:#fff;position:relative}
a{color:inherit;text-decoration:none}
.abs{position:absolute}

/* hero */
.hero{left:0;top:0;width:736px;height:341px;background:radial-gradient(ellipse at 40% 30%,#f7f7f7 0%,var(--hero-top) 40%,var(--hero-bottom) 100%)}
.brand{left:108px;top:16px;display:flex;align-items:center;gap:6px;font-size:30px;color:#4a4a4a;letter-spacing:-0.5px}
.brand-dot{width:22px;height:22px;border-radius:50%;background:var(--blue)}
.topbar{right:104px;top:9px;display:flex;align-items:center;gap:8px;font-size:8px;color:#444}
.topbar .pill{background:#fff;border-radius:2px;padding:2px 6px;font-size:7.5px}
.topbar .sep{color:#aaa}
.topbar .social{font-size:7px;color:var(--muted)}
.nav{left:321px;top:37px;display:flex;gap:15px;font-size:7.5px;color:#555}
.nav .active{color:var(--blue)}
.dropdown{left:357px;top:54px;width:70px;background:#fff;border-radius:2px;padding:4px 6px;font-size:6.5px;color:#888;line-height:11.6px;box-shadow:0 1px 2px rgba(0,0,0,.05)}
.dropdown .current{color:#333}
.quote{left:124px;top:149px;width:230px;font-size:8.6px;line-height:11.8px;color:#333}
.quote b{font-weight:700}
.quote-mark{font-size:26px;color:#bbb;font-family:Georgia,serif;line-height:1}
.author{left:124px;top:214px;width:240px;font-size:8px;line-height:12px}
.author b{font-weight:700;font-size:8.2px}
.author-rule{left:197px;top:219px;width:137px;height:1px;background:#bbb}
.btn-hero{top:257px;height:18px;border-radius:2px;color:#fff;font-size:8.8px;display:flex;align-items:center;justify-content:center;gap:4px}
.btn-hero .ring{width:9px;height:9px;border:1.2px solid #fff;border-radius:50%}
.btn-case{left:124px;width:78px;background:var(--blue);border:1px solid var(--blue-dark)}
.btn-buy{left:210px;width:44px;background:var(--green);border:1px solid #6a9a27}
.hero-art{left:409px;top:133px;width:222px;height:154px;border-radius:80px 90px 30px 30px;background:radial-gradient(ellipse at 50% 40%,#e3f4fd 0%,var(--sky) 70%,#4aa9dd 100%)}

/* welcome */
.welcome-title{left:0;top:389px;width:736px;text-align:center;font-size:16px;color:#333}
.welcome-title span{color:var(--blue)}
.welcome-copy{left:128px;top:428px;width:480px;text-align:center;font-size:7.2px;line-height:11.6px;color:#444}
.welcome-copy p+p{margin-top:12px}
.btn-read{left:336px;top:560px;width:64px;height:19px;background:var(--blue);border:1px solid var(--blue-dark);border-radius:2px;color:#fff;font-size:8.6px;display:flex;align-items:center;justify-content:center}

/* features */
.features{left:0;top:629px;width:736px;height:302px;background:var(--light);border-top:1px solid #ececec}
.feature{top:671px;width:170px;text-align:center}
.feature h3{font-weight:400;font-size:11px;color:var(--blue)}
.feature .art{margin:11px auto 0;width:120px;height:96px;border-radius:6px}
.feature p{margin-top:14px;font-size:6.6px;line-height:12.6px;color:#444}
.feature .btn-more{display:inline-block;margin-top:10px;padding:3px 6px;border:1px solid #ccc;background:#fff;font-size:6.8px;color:var(--blue);border-radius:1px}
.art-devices{background:linear-gradient(160deg,#bfe6fa,#e9eef2 60%,#fafafa)}
.art-cloud{background:radial-gradient(ellipse at 50% 50%,#e6f5fd,var(--sky) 90%)}
.art-diagram{background:radial-gradient(ellipse at 50% 50%,#eef7fb,#c5e3f2 80%)}

/* partners */
.partners{left:0;top:931px;width:736px;height:67px;display:flex;align-items:center;justify-content:center;gap:22px}
.partner{height:14px;background:#b9b9b9;border-radius:2px}
.partner.round{width:32px;height:32px;border-radius:50%;background:#8d8d8d}

/* footer */
.footer{left:0;top:998px;width:736px;height:177px;background:var(--footer)}
.fcol{top:1030px}
.fcol h4{font-weight:400;font-size:10.8px;color:#fff;margin-bottom:10px}
.fcol ul{list-style:none;font-size:6.8px;line-height:14.7px;color:var(--footer-text)}
.fcol li::before{content:"";display:inline-block;width:2px;height:2px;background:#aaa;border-radius:50%;margin:0 5px 1px 1px;vertical-align:middle}
.footbar{left:0;top:1175px;width:736px;height:25px;background:var(--footer-bar);color:#ddd}
.foot-brand{left:106px;top:1179px;font-size:15px;color:#9a9a9a}
.foot-copy{left:177px;top:1185px;font-size:6px;color:#9a9a9a}
.foot-contact{right:106px;top:1183px;display:flex;gap:8px;align-items:center;font-size:7.6px;color:#fff}
.foot-contact .social{font-size:6.4px;color:#ccc}
</style>
</head>
<body>

<section class="abs hero"></section>
<div class="abs brand"><span class="brand-dot"></span>vorlu.</div>

<div class="abs topbar">
  <svg width="8" height="8" viewBox="0 0 10 10"><path d="M2 1l2 2-1 1.5c.6 1.2 1.5 2 2.5 2.5L7 6l2 2-1.5 1.5C4 9 1 6 .5 2z" fill="#2a86c8"/></svg>
  <span>+61 (0)4000 555 210</span><span class="sep">•</span>
  <svg width="9" height="7" viewBox="0 0 9 7"><rect width="9" height="7" fill="#2a86c8"/><path d="M0 0l4.5 3.5L9 0" stroke="#fff" fill="none" stroke-width=".8"/></svg>
  <span>mara@vorlu.com</span>
  <a class="pill" href="#">Support</a><a class="pill" href="#">Login</a>
  <span class="social">Chirpnest · WorkWeave</span>
</div>

<nav class="abs nav">
  <a class="active" href="#">Home</a><a href="#">Products +</a><a href="#">Company</a><a href="#">Technology Partners</a><a href="#">Press/News</a><a href="#">ContactUs</a>
</nav>
<div class="abs dropdown">
  <div>Product One</div><div>Product Two</div><div class="current">Product Three</div><div>Product Four</div>
</div>

<svg class="abs" style="left:41px;top:145px" width="18" height="36" viewBox="0 0 18 36"><path d="M16 1L2 18l14 17" stroke="#aaa" fill="none" stroke-width="1"/></svg>
<svg class="abs" style="left:677px;top:145px" width="18" height="36" viewBox="0 0 18 36"><path d="M2 1l14 17L2 35" stroke="#aaa" fill="none" stroke-width="1"/></svg>

<div class="abs quote-mark" style="left:103px;top:146px">“</div>
<div class="abs quote">Lorem ipsum dolor sit amet, consectetur adipiscing elit. Sed id tempus enim. <b>Etiam eros velit, rutrum in fringilla id, fermentum sit amet nulla.</b> Nullam cursus lorem commodo eu pharetra elit blandit.</div>
<div class="abs author"><b>Dictum id tellus</b><br>Vestibulum ante ipsum primis</div>
<div class="abs author-rule"></div>
<div class="abs quote-mark" style="left:343px;top:208px">”</div>
<a class="abs btn-hero btn-case" href="#">Case Studies <span class="ring"></span></a>
<a class="abs btn-hero btn-buy" href="#">Buy <span class="ring"></span></a>
<div class="abs hero-art" role="img" aria-label="Illustration of a blue cloud with a golden key in a lock"></div>

<h2 class="abs welcome-title" style="font-weight:400">Welcome to <span>vorlu</span></h2>
<div class="abs welcome-copy">
  <p>Lorem ipsum dolor sit amet, consectetur adipiscing elit. Nulla lobortis consequat mauris, eget eleifend nunc viverra viverra. Ut ac risus odio. Aliquam pretium purus sed nulla feugiat blandit. Cras vel libero ut lacus eleifend tempor. Phasellus eleifend, magna non tincidunt accumsan, justo arcu cursus ipsum, non porttitor sapien</p>
  <p>Quam vel magna. Maecenas elit nisl, molestie nec dapibus nec, aliquet a erat. Donec scelerisque lacus a libero suscipit auctor volutpat enim euismod. Mauris porta, lacus ut ullamcorper sodales, mauris tortor feugiat purus, nec aliquam neque purus ac metus. Nunc eleifend leo quis nisl hendrerit ultrices. Suspendisse quis feugiat elit. Fusce vitae dolor ac est tincidunt feugiat. Phasellus volutpat dui in sapien malesuada tempus placerat justo ultricies. Duis mollis ornare risus, ut consectetur mi tincidunt sit amet. Maecenas quis nibh ac orci tempus scelerisque ac et massa.</p>
</div>
<a class="abs btn-read" href="#">Read More</a>

<section class="abs features"></section>
<div class="abs feature" style="left:97px">
  <h3>Consectetur adipiscing</h3>
  <div class="art art-devices" role="img" aria-label="Illustration of a cloud linked to computers, laptops and phones"></div>
  <p>Vestibulum ante ipsum primis in faucibus orci luctus et ultrices posuere cubilia Vestibulum ac nibh eget enim sollicitudin tincidunt et ac lorem. Cras eget sollicitudin lectus. In vel turpis lacus, vitae fringilla urna.</p>
  <a class="btn-more" href="#">Read More</a>
</div>
<div class="abs feature" style="left:283px">
  <h3>Nulla lobortis consequat</h3>
  <div class="art art-cloud" role="img" aria-label="Illustration of a blue cloud with a laptop in front"></div>
  <p>Phasellus malesuada, massa et adipiscing tempor, tellus lacus vulputate dui, non commodo mi neque a dui. Praesent enim dolor, iaculis ut molestie vitae, tempus vitae tortor. Vestibulum ante ipsum primis in faucibus orci</p>
  <a class="btn-more" href="#">Read More</a>
</div>
<div class="abs feature" style="left:463px;width:180px">
  <h3>Duis nec augue eget</h3>
  <div class="art art-diagram" style="width:140px" role="img" aria-label="Diagram of cloud security risks linked by arrows"></div>
  <p>Nam quis ligula a nibh fermentum venenatis vitae nec neque. Etiam non felis mi. Quisque feugiat, lectus non feugiat consectetur, purus ipsum lobortis nisl, a sollicitudin risus arcu elementum risus. Sed feugiat mollis neque.</p>
  <a class="btn-more" href="#">Read More</a>
</div>

<div class="abs partners">
  <div class="partner" style="width:64px"></div>
  <div class="partner" style="width:54px;height:18px"></div>
  <div class="partner" style="width:56px"></div>
  <div class="partner round"></div>
  <div class="partner" style="width:54px"></div>
  <div class="partner" style="width:52px"></div>
  <div class="partner" style="width:72px"></div>
</div>

<footer class="abs footer"></footer>
<div class="abs fcol" style="left:105px"><h4>How We Help</h4><ul><li>Nulla lobortis</li><li>Consequat mauris</li><li>Eget eleifend</li><li>Duis nec augue</li><li>Lectus non</li></ul></div>
<div class="abs fcol" style="left:201px"><h4>Services</h4><ul><li>Ultricies eleifend</li><li>Duis nec augue eget</li><li>Lorem vestibulum suscipit</li><li>Integer eget ligula</li></ul></div>
<div class="abs fcol" style="left:326px"><h4>Products</h4><ul><li>Nulla lobortis</li><li>Consequat mauris</li><li>Eget eleifend</li><li>Duis nec augue</li><li>Lectus non</li></ul></div>
<div class="abs fcol" style="left:438px"><h4>Results</h4><ul><li>Donec a lectus</li><li>Adipiscing</li><li>Lorem vestibulum</li><li>Nulla lobortis consequat</li><li>Consectetur</li><li>Lorem ipsum</li><li>Ultricies eleifend</li></ul></div>
<div class="abs fcol" style="left:549px"><h4>Links</h4><ul><li>Privacy Policy</li><li>Terms of Use</li><li>Contact Us</li><li>Sitemap</li></ul></div>

<div class="abs footbar"></div>
<div class="abs foot-brand">vorlu.</div>
<div class="abs foot-copy">© Copyright 2014 vorlu.com. All Rights Reserved</div>
<div class="abs foot-contact">
  <svg width="8" height="8" viewBox="0 0 10 10"><path d="M2 1l2 2-1 1.5c.6 1.2 1.5 2 2.5 2.5L7 6l2 2-1.5 1.5C4 9 1 6 .5 2z" fill="#fff"/></svg>
  <span>+61 (0)4000 555 210</span><span style="color:#999">•</span>
  <svg width="9" height="7" viewBox="0 0 9 7"><rect width="9" height="7" fill="#fff"/><path d="M0 0l4.5 3.5L9 0" stroke="#414143" fill="none" stroke-width=".8"/></svg>
  <span>mara@vorlu.com</span>
  <span class="social">Chirpnest · WorkWeave</span>
</div>

</body>
</html>
```